New business card design needed for Trucking/Staffing company!

I am looking for a business card design. The business name is Harbor Lane Freightworks, LLC. This company is a staffing company for commercial drivers/truck drivers. Most of our customers are trucking/supply companies. Our colors are blue/black/white/grey. The info I have on my current business cards is
-Spot for a name
-2 lines for an address
-3 lines for Office, cell, and fax
-email
-website(currently on backside of card with logo but can go anywhere)
Updates

Project Deadline Extended
Reason: Open to more designs

Target Market(s)

Trucking companies, building supply companies

Industry/Entity Type

Business

Contact Information for Business Card

Edgy but professional

Font styles to use
Other font styles liked:
• Open to suggestions

Colors
0555a3
000000
ffffff
9d9d9d

Requirements
Must have
• Must have the logo incorporated

```html
<!DOCTYPE html>
<html lang="en">
<head>
<meta charset="utf-8">
<title>Harbor Lane Freightworks, LLC — Business Card</title>
<link href="https://fonts.googleapis.com/css2?family=Exo+2:wght@400;600;700&display=swap" rel="stylesheet">
<style>
  :root {
    --backdrop: #9a9a9a;
    --card-white: #f2f2f3;
    --card-black: #1b1a1a;
    --brand-blue: #232f8f;
    --brand-blue-bright: #3344b0;
    --ink: #3a3a3c;
    --ink-soft: #555558;
    --rule-grey: #9d9d9d;
    --art-light: #e4e4e6;
    --art-mid: #cfcfd2;
    --web-grey: #d6d6d6;
  }
  * { box-sizing: border-box; margin: 0; padding: 0; }
  html, body {
    width: 1105px;
    height: 1200px;
    overflow: hidden;
    background: var(--backdrop);
    font-family: "Exo 2", sans-serif;
  }
  .sheet {
    position: relative;
    width: 1105px;
    height: 1200px;
  }
  .card {
    position: absolute;
    left: 182px;
    width: 748px;
    height: 426px;
    overflow: hidden;
  }
  .card--front { top: 120px; background: var(--card-white); }
  .card--back { top: 637px; background: var(--card-black); }

  /* Front */
  .front-art {
    position: absolute;
    left: 280px;
    top: 18px;
    width: 440px;
    height: 400px;
    background: radial-gradient(ellipse at 60% 55%, var(--art-mid) 0%, var(--art-light) 45%, var(--card-white) 75%);
  }
  .wordmark {
    position: absolute;
    left: 36px;
    top: 34px;
    color: var(--brand-blue);
    font-weight: 700;
    text-transform: uppercase;
    line-height: 1;
  }
  .wordmark__main { display: block; font-size: 30px; letter-spacing: 1px; }
  .wordmark__sub { display: block; font-size: 15px; letter-spacing: 2px; margin-top: 6px; }
  .person {
    position: absolute;
    left: 36px;
    top: 108px;
  }
  .person__name {
    color: var(--brand-blue);
    font-size: 26px;
    font-weight: 600;
    line-height: 1.2;
  }
  .person__title {
    color: var(--ink);
    font-size: 19px;
    margin-top: 2px;
  }
  .address {
    position: absolute;
    left: 36px;
    top: 186px;
    color: var(--ink-soft);
    font-size: 19px;
    line-height: 26px;
    font-style: normal;
  }
  .contacts {
    position: absolute;
    left: 36px;
    top: 252px;
    list-style: none;
    color: var(--ink-soft);
    font-size: 19px;
  }
  .contacts__item {
    display: flex;
    align-items: center;
    height: 29px;
  }
  .contacts__icon {
    width: 18px;
    height: 18px;
    margin-right: 11px;
    fill: var(--brand-blue);
    flex: none;
  }

  /* Back */
  .back-mark {
    position: absolute;
    left: 0;
    right: 0;
    top: 168px;
    text-align: center;
    color: var(--brand-blue-bright);
    font-weight: 700;
    font-size: 34px;
    letter-spacing: 2px;
    text-transform: uppercase;
  }
  .back-web {
    position: absolute;
    left: 0;
    right: 0;
    top: 356px;
    text-align: center;
    color: var(--web-grey);
    font-size: 19px;
    letter-spacing: 6px;
  }
</style>
</head>
<body>
<main class="sheet">
  <section class="card card--front" aria-label="Business card front">
    <div class="front-art" role="img" aria-label="Line-drawn truck cab illustration"></div>
    <div class="wordmark">
      <span class="wordmark__main">Harbor Lane</span>
      <span class="wordmark__sub">Freightworks, LLC</span>
    </div>
    <div class="person">
      <p class="person__name">Daniel Reyes</p>
      <p class="person__title">CEO/Founder</p>
    </div>
    <address class="address">412 Kestrel Road<br>Juneau, Alaska 99801</address>
    <ul class="contacts">
      <li class="contacts__item">
        <svg class="contacts__icon" viewBox="0 0 24 24"><path d="M6.6 10.8c1.4 2.8 3.8 5.1 6.6 6.6l2.2-2.2c.3-.3.7-.4 1-.2 1.1.4 2.3.6 3.6.6.6 0 1 .4 1 1V20c0 .6-.4 1-1 1C10.6 21 3 13.4 3 4c0-.6.4-1 1-1h3.5c.6 0 1 .4 1 1 0 1.3.2 2.5.6 3.6.1.3 0 .7-.2 1L6.6 10.8z"/></svg>
        555 201 4417
      </li>
      <li class="contacts__item">
        <svg class="contacts__icon" viewBox="0 0 24 24"><path d="M7 1h10c1.1 0 2 .9 2 2v18c0 1.1-.9 2-2 2H7c-1.1 0-2-.9-2-2V3c0-1.1.9-2 2-2zm0 3v14h10V4H7zm5 15.5a1.2 1.2 0 1 0 0 2.4 1.2 1.2 0 0 0 0-2.4z"/></svg>
        555 318 2290
      </li>
      <li class="contacts__item">
        <svg class="contacts__icon" viewBox="0 0 24 24"><path d="M6 2h10l2 2v5H6V2zm-3 8h18c1.1 0 2 .9 2 2v8H1v-8c0-1.1.9-2 2-2zm3 4v2h4v-2H6zm6 0v2h2v-2h-2zm4 0v2h2v-2h-2z"/></svg>
        555 764 0153
      </li>
      <li class="contacts__item">
        <svg class="contacts__icon" viewBox="0 0 24 24"><path d="M2 5h20v14H2V5zm2 2v.5l8 5 8-5V7H4zm0 2.9V17h16V9.9l-8 5-8-5z"/></svg>
        dan@harborlanefw.com
      </li>
      <li class="contacts__item">
        <svg class="contacts__icon" viewBox="0 0 24 24"><path d="M12 2a10 10 0 1 0 0 20 10 10 0 0 0 0-20zm-1 17.9A8 8 0 0 1 4.2 10l4.8 4.8v1c0 1.1.9 2 2 2v2.1zm6.9-2.5c-.3-.8-1-1.4-1.9-1.4h-1v-3c0-.6-.4-1-1-1H8v-2h2c.6 0 1-.4 1-1V7h2c1.1 0 2-.9 2-2v-.4a8 8 0 0 1 2.9 12.8z"/></svg>
        www.harborlanefw.com
      </li>
    </ul>
  </section>

  <section class="card card--back" aria-label="Business card back">
    <p class="back-mark">Harbor Lane Freightworks, LLC</p>
    <p class="back-web">www.harborlanefw.com</p>
  </section>
</main>
</body>
</html>
```